Coffee Pouch Label for Coffee Roaster

We are wanting some new labels for our coffee pouches.
We are an established, small family owned specialty coffee roaster called Tarn4 Coffee Roasters, and we are located in Kestrel Vale, NSW Australia.
Label dimensions are 100 x 150mm, to fit on a couple of different bag sizes. We use coffee pouches with kraft paper finish.
We have 3 main blends, Lanternfly, Quillrock & Pale Finch, and a range of rotating single origin coffees. We would get labels printed for the blends, but then need a 'generic' design that we can either write the name on, or stick another sticker over for the single origin coffees.
Some information that needs to be on the label:
our logo
web address: www.tarn4coffee.example
address: 47 Corvell St, Kestrel Vale, NSW
Proudly Roasted in Kestrel Vale, NSW
Blend name
our tagline/mission: Roast Kindly | Share Warmly | Brew Honestly
statement: We give $1 from every kg of coffee sold to groups that shelter, protect and support children in need.
We would like to use colour to help differentiate the different blends somehow.
We are after a creative, clean design, that is representative of specialty coffee (not large commercial coffee brands).
I have uploaded our logo both with and without our tagline, and also some other packaging inspiration that i like (I quite like the meadow coffee label design).
thanks everyone!
Marcus
People who appreciate good, local coffee

```html
<!DOCTYPE html>
<html lang="en">
<head>
<meta charset="utf-8">
<title>Tarn4 Coffee Roasters – Blend Labels</title>
<link rel="stylesheet" href="https://fonts.googleapis.com/css2?family=Bebas+Neue&family=Open+Sans:wght@400;700&display=swap">
<style>
  :root {
    --backdrop: #eeeeee;
    --kraft: #b88d66;
    --kraft-shade: #a97e58;
    --ink: #2a221d;
    --band-lanternfly: #a6dfe5;
    --band-quillrock: #f5cdbd;
    --band-palefinch: #f1efbd;
  }
  * { box-sizing: border-box; margin: 0; padding: 0; }
  html, body { width: 1200px; height: 800px; overflow: hidden; }
  body {
    background: var(--backdrop);
    font-family: "Open Sans", sans-serif;
    color: var(--ink);
  }
  .label-row {
    position: absolute;
    top: 175px;
    left: 120px;
    display: flex;
    gap: 30px;
  }
  .label {
    position: relative;
    width: 300px;
    height: 450px;
    background: var(--kraft);
    text-align: center;
  }
  .brand {
    position: absolute;
    top: 42px;
    left: 0;
    right: 0;
  }
  .brand-name {
    font-weight: 700;
    font-size: 34px;
    line-height: 1;
    letter-spacing: 1px;
  }
  .brand-sub {
    font-size: 7px;
    font-weight: 700;
    letter-spacing: 2px;
    margin-top: 3px;
  }
  .tagline {
    font-size: 6.5px;
    margin-top: 2px;
  }
  .blend-band {
    position: absolute;
    top: 126px;
    left: 36px;
    width: 228px;
    height: 70px;
    display: flex;
    align-items: center;
    justify-content: center;
    font-family: "Bebas Neue", sans-serif;
    font-weight: 400;
    font-size: 44px;
    letter-spacing: 1px;
    padding-top: 4px;
  }
  .label--lanternfly .blend-band { background: var(--band-lanternfly); }
  .label--quillrock .blend-band { background: var(--band-quillrock); }
  .label--palefinch .blend-band { background: var(--band-palefinch); }
  .roasted-in {
    position: absolute;
    top: 222px;
    left: 0;
    right: 0;
    font-family: "Bebas Neue", sans-serif;
    font-size: 13px;
    letter-spacing: 0.5px;
  }
  .mission {
    position: absolute;
    top: 262px;
    left: 100px;
    width: 100px;
    height: 100px;
  }
  .mission-ring {
    position: absolute;
    inset: 0;
    border-radius: 50%;
    background: radial-gradient(circle, var(--kraft) 58%, var(--kraft-shade) 62%, var(--kraft) 72%);
  }
  .mission-text {
    position: absolute;
    top: 24px;
    left: 12px;
    right: 12px;
    font-size: 6px;
    line-height: 1.35;
  }
  .contact {
    position: absolute;
    top: 392px;
    left: 0;
    right: 0;
    font-size: 8px;
    line-height: 1.4;
  }
  .contact-web { font-weight: 700; }
</style>
</head>
<body>
  <main class="label-row">
    <section class="label label--lanternfly">
      <header class="brand">
        <div class="brand-name">Tarn4</div>
        <div class="brand-sub">COFFEE ROASTERS</div>
        <div class="tagline">Roast Kindly | Share Warmly | Brew Honestly</div>
      </header>
      <h2 class="blend-band">LANTERNFLY</h2>
      <p class="roasted-in">PROUDLY ROASTED IN KESTREL VALE, NSW</p>
      <div class="mission">
        <div class="mission-ring" role="img" aria-label="Coffee cup ring stain with two coffee beans"></div>
        <p class="mission-text">We give $1 from every kg of coffee sold to groups that shelter, protect and support children in need.</p>
      </div>
      <footer class="contact">
        <div class="contact-web">www.tarn4coffee.example</div>
        <div>47 Corvell St, Kestrel Vale, NSW</div>
      </footer>
    </section>

    <section class="label label--quillrock">
      <header class="brand">
        <div class="brand-name">Tarn4</div>
        <div class="brand-sub">COFFEE ROASTERS</div>
        <div class="tagline">Roast Kindly | Share Warmly | Brew Honestly</div>
      </header>
      <h2 class="blend-band">QUILLROCK</h2>
      <p class="roasted-in">PROUDLY ROASTED IN KESTREL VALE, NSW</p>
      <div class="mission">
        <div class="mission-ring" role="img" aria-label="Coffee cup ring stain with two coffee beans"></div>
        <p class="mission-text">We give $1 from every kg of coffee sold to groups that shelter, protect and support children in need.</p>
      </div>
      <footer class="contact">
        <div class="contact-web">www.tarn4coffee.example</div>
        <div>47 Corvell St, Kestrel Vale, NSW</div>
      </footer>
    </section>

    <section class="label label--palefinch">
      <header class="brand">
        <div class="brand-name">Tarn4</div>
        <div class="brand-sub">COFFEE ROASTERS</div>
        <div class="tagline">Roast Kindly | Share Warmly | Brew Honestly</div>
      </header>
      <h2 class="blend-band">PALE FINCH</h2>
      <p class="roasted-in">PROUDLY ROASTED IN KESTREL VALE, NSW</p>
      <div class="mission">
        <div class="mission-ring" role="img" aria-label="Coffee cup ring stain with two coffee beans"></div>
        <p class="mission-text">We give $1 from every kg of coffee sold to groups that shelter, protect and support children in need.</p>
      </div>
      <footer class="contact">
        <div class="contact-web">www.tarn4coffee.example</div>
        <div>47 Corvell St, Kestrel Vale, NSW</div>
      </footer>
    </section>
  </main>
</body>
</html>
```